Granger Earthworks LLC business card design

Excavation company business cards

Contact Information for Business Card

Granger Earthworks LLC cell phone 208-555-0147 office phone 208-555-0193 grangerearthworksllc@mailnest.example Driveways, site prep, retaining walls, septic systems, rock delivery

Colors

Designer to choose colors to be used in the design.

```html
<!DOCTYPE html>
<html lang="en">
<head>
<meta charset="utf-8">
<title>Granger Earthworks LLC – Business Card</title>
<link href="https://fonts.googleapis.com/css2?family=Montserrat:wght@400;500;600;800&display=swap" rel="stylesheet">
<style>
  :root {
    --orange: #e36b22;
    --orange-dark: #c9561a;
    --orange-light: #ec8a4e;
    --card-white: #ececec;
    --ink: #4a4a4a;
    --rule: #b9b9b9;
    --stripe: #5a5a5a;
    --backdrop: #d4d4d4;
  }
  * { margin: 0; padding: 0; box-sizing: border-box; }
  html, body {
    width: 1084px; height: 1200px; overflow: hidden;
    background: var(--backdrop);
    font-family: "Montserrat", sans-serif;
  }
  .sheet {
    width: 1084px; height: 1200px;
    display: flex; flex-direction: column; align-items: center; justify-content: center;
    gap: 60px;
  }
  .card {
    position: relative;
    width: 880px; height: 504px;
    border-radius: 30px;
    overflow: hidden;
    box-shadow: 0 6px 14px rgba(0,0,0,0.25);
  }

  /* Front */
  .card-front { background: var(--orange); }
  .front-pattern {
    position: absolute; inset: 0;
    background: radial-gradient(ellipse at 75% 30%, var(--orange-light) 0%, var(--orange) 55%, var(--orange-dark) 100%);
  }
  .front-brand {
    position: absolute; left: 50%; top: 50%;
    transform: translate(-50%, -50%);
    display: flex; align-items: center; gap: 14px;
    color: #fff; font-weight: 800; font-size: 34px; letter-spacing: 1px;
    white-space: nowrap;
  }
  .brand-dot { width: 16px; height: 16px; border-radius: 50%; background: currentColor; }

  /* Back */
  .card-back { background: var(--card-white); }
  .back-brand {
    position: absolute; left: 72px; top: 92px;
    display: flex; align-items: center; gap: 14px;
    color: var(--orange); font-weight: 800; font-size: 34px; letter-spacing: 0.5px;
  }
  .person {
    position: absolute; right: 64px; top: 226px; text-align: right;
  }
  .person-name { color: var(--orange); font-weight: 600; font-size: 31px; line-height: 1.1; }
  .person-title { color: var(--ink); font-weight: 500; font-size: 22px; margin-top: 4px; }
  .divider {
    position: absolute; left: 55px; right: 64px; top: 300px;
    height: 2px; background: var(--rule);
  }
  .contacts {
    position: absolute; left: 55px; top: 312px;
    list-style: none;
  }
  .contacts li {
    display: flex; align-items: center; gap: 16px;
    color: var(--ink); font-size: 20px; line-height: 29px;
  }
  .contacts svg { width: 16px; height: 16px; flex: none; }
  .services {
    position: absolute; left: 0; right: 0; bottom: 0; height: 40px;
  }
  .services svg { position: absolute; inset: 0; width: 100%; height: 100%; }
  .services-text {
    position: absolute; left: 0; right: 0; top: 0; height: 40px;
    display: flex; align-items: center; justify-content: center;
    color: #fff; font-size: 14.5px; font-weight: 500; letter-spacing: 0.2px;
  }
</style>
</head>
<body>
<main class="sheet">

  <section class="card card-front" aria-label="Card front">
    <div class="front-pattern" role="img" aria-label="Repeating tone-on-tone pattern of the company emblem"></div>
    <div class="front-brand"><span class="brand-dot"></span>Granger Earthworks LLC</div>
  </section>

  <section class="card card-back" aria-label="Card back">
    <div class="back-brand"><span class="brand-dot"></span>Granger Earthworks LLC</div>

    <div class="person">
      <div class="person-name">Dale Harmon</div>
      <div class="person-title">President</div>
    </div>

    <div class="divider"></div>

    <ul class="contacts">
      <li>
        <svg viewBox="0 0 16 16"><path d="M3 1.5l3 3-1.6 1.8c.9 2 2.4 3.5 4.3 4.3L10.5 9l3 3-2 2.3C6.5 14 2 9.5 1.7 3.5z" fill="var(--orange)"/></svg>
        208-555-0147
      </li>
      <li>
        <svg viewBox="0 0 16 16"><path d="M3 1.5l3 3-1.6 1.8c.9 2 2.4 3.5 4.3 4.3L10.5 9l3 3-2 2.3C6.5 14 2 9.5 1.7 3.5z" fill="var(--orange)"/></svg>
        208-555-0193
      </li>
      <li>
        <svg viewBox="0 0 16 16"><rect x="1" y="3" width="14" height="10" rx="1" fill="var(--orange)"/><path d="M1.5 3.5L8 9l6.5-5.5" stroke="#fff" stroke-width="1.3" fill="none"/></svg>
        grangerearthworksllc@mailnest.example
      </li>
      <li>
        <svg viewBox="0 0 16 16"><circle cx="8" cy="8" r="6.5" fill="none" stroke="var(--orange)" stroke-width="1.5"/><ellipse cx="8" cy="8" rx="3" ry="6.5" fill="none" stroke="var(--orange)" stroke-width="1.2"/><path d="M1.5 8h13M2.5 5h11M2.5 11h11" stroke="var(--orange)" stroke-width="1.1"/></svg>
        GrangerEarthworks.example
      </li>
    </ul>

    <div class="services">
      <svg viewBox="0 0 880 40" preserveAspectRatio="none" aria-hidden="true">
        <g fill="var(--stripe)">
          <polygon points="0,40 14,12 28,12 14,40"/>
          <polygon points="32,40 46,12 60,12 46,40"/>
          <polygon points="64,40 78,12 92,12 78,40"/>
          <polygon points="796,40 810,12 824,12 810,40"/>
          <polygon points="828,40 842,12 856,12 842,40"/>
          <polygon points="860,40 874,12 888,12 874,40"/>
        </g>
        <polygon points="96,40 110,12 792,12 778,40" fill="var(--orange)"/>
      </svg>
      <div class="services-text" style="top:12px;height:28px;">DRIVEWAYS • SITE PREP • RETAINING WALLS • SEPTIC SYSTEMS • ROCK DELIVERY</div>
    </div>
  </section>

</main>
</body>
</html>
```